Redesign Canvas Art E-Commerce Website

Help! I hired a couple of companies on Tasklyn.com to build and design an e-commerce website for me. After three long and painful months, I have one that I believe is functional on the back-end, but aesthetically on the front end is a mess.

We are a small family business that will take your digital photo and manipulate it into a digitally created oil, watercolor or impressionist style pieces of artwork that we print on museum quality, gallery grade canvas and ship to the customer, ready to hang.

We are looking to create an e-commerce website where a customer can choose their art style, upload a photo, choose their canvas size and orientation (horizontal or vertical) and checkout. Within 48 hours, we will send them back a proof of their newly created, customized artwork for them to approve or not approve. If they approve, we print, package and ship them the product. If they do not approve, we offer unlimited revisions until they are happy.

As I mentioned, the back end functionality is already there, just need design help. No coding required

Here is a link to the development page that they created: https://brushvellomart.com/development/

As you can see, it looks off...doesnt line up properly, wasted space, weird font. Feel free to either correct the homepage they created or design an entirely new page. I am attaching some examples of before and after photos of artwork for reference. I also think the testimonials page and shop page can use a little style. The content is there and accurate, it just doesn't look pretty. Please keep in mind that our customers will probably not be very tech savvy. The customers will probably be sending us pics of kids, grandkids, pets, family portraits, vacation photos, etc.

Here is one of our competitors - www.pelfandquill.com
Their website looks clean and inviting.

Thank you in advance! Im looking forward to seeing the results. I am including our logo in the attachments (I do not have it in a vector file, just a jpeg)

Target Market(s)

Non tech-savvy indiduals, 30-70 years old

Industry/Entity Type

Please look at https://brushvellomart.com/development/ to see various pages and what the other designers did

Number of Pages Required

1 page

Requirements
Must have
• Verbiage on pages leave "as is" but feel free to change styles. Would like to keep existing four categories on homepage
Nice to have
• Warm and inviting homepage that evokes emotion

```html
<!DOCTYPE html>
<html lang="en">
<head>
<meta charset="utf-8">
<title>Brushvello Art – Turn Your Digital Photos Into Wall Art</title>
<link rel="stylesheet" href="https://fonts.googleapis.com/css2?family=Lato:wght@400;700;900&family=Poppins:wght@500;600&display=swap">
<style>
  :root {
    --brand-red: #e8435a;
    --navy: #2b3467;
    --cream: #fdfee9;
    --frame-blue: #b7d7e8;
    --ink: #1c1c28;
    --white: #ffffff;
  }
  * { margin: 0; padding: 0; box-sizing: border-box; }
  html, body { width: 1200px; height: 3333px; overflow: hidden; }
  body {
    position: relative;
    background: var(--cream);
    font-family: "Lato", Arial, sans-serif;
    color: var(--navy);
  }
  .abs { position: absolute; }

  /* Header */
  .site-header { left: 0; top: 0; width: 1200px; height: 142px; background: var(--brand-red); }
  .brand { display: flex; align-items: center; gap: 10px; }
  .brand-dot { width: 26px; height: 26px; border-radius: 50%; background: var(--ink); }
  .brand-name { font-family: "Lato", sans-serif; font-weight: 900; color: var(--ink); }
  .site-header .brand { left: 133px; top: 52px; }
  .site-header .brand-name { font-size: 30px; }
  .main-nav { left: 388px; top: 58px; display: flex; gap: 24px; }
  .main-nav a { color: var(--white); text-decoration: none; font-size: 20px; }

  /* Hero */
  .hero-title { left: 0; top: 197px; width: 1200px; text-align: center; font-weight: 900; font-size: 55px; line-height: 65px; color: var(--navy); letter-spacing: -0.5px; }
  .accent { color: var(--brand-red); }
  .hero-collage {
    left: 130px; top: 383px; width: 936px; height: 330px;
    background: linear-gradient(90deg, #8a7a63 0%, #d9a56e 30%, #7fa36a 60%, #c9b79a 85%, #e9d6c2 100%);
  }
  .section-heading { left: 0; width: 1200px; text-align: center; font-weight: 900; color: var(--navy); text-transform: uppercase; }
  .tagline { top: 780px; font-size: 42px; line-height: 49px; }

  .feature-frame { left: 335px; top: 911px; width: 561px; height: 581px; background: var(--frame-blue); box-shadow: 0 3px 6px rgba(0,0,0,0.2); }
  .feature-art { left: 22px; top: 18px; width: 518px; height: 544px; background: linear-gradient(135deg, #efeae0 0%, #c27a3a 45%, #3b2a1e 70%, #d8cdbf 100%); }
  .btn {
    display: flex; align-items: center; justify-content: center;
    background: var(--brand-red); color: var(--white); font-weight: 700;
    border-radius: 8px; box-shadow: 0 3px 5px rgba(0,0,0,0.2); text-decoration: none;
  }
  .btn-start { left: 149px; top: 484px; width: 263px; height: 67px; font-size: 31px; }

  /* Categories */
  .categories-title { top: 1537px; font-size: 44px; }
  .category-card { top: 1637px; width: 222px; height: 221px; border-radius: 14px; box-shadow: 0 2px 6px rgba(0,0,0,0.25); }
  .cat-oil { left: 133px; background: linear-gradient(160deg, #3d4a22, #a0542c 60%, #e9e2d6); }
  .cat-water { left: 369px; background: linear-gradient(160deg, #f3d9cf, #fbf3ee 60%, #e8c2b4); }
  .cat-digital { left: 608px; background: linear-gradient(160deg, #dfe6dc, #8ab07c 50%, #5f86b0); }
  .cat-impress { left: 845px; background: linear-gradient(160deg, #4a2e1c, #c79a73 50%, #e9e4b8); }
  .category-btn { top: 1873px; width: 154px; height: 37px; font-size: 20px; }

  /* About */
  .about-title { top: 1978px; font-size: 44px; }
  .about-copy { left: 178px; top: 2058px; width: 844px; text-align: center; font-family: "Poppins", sans-serif; font-weight: 600; font-size: 15px; line-height: 17px; text-transform: uppercase; color: var(--navy); }
  .about-copy p { margin-bottom: 16px; }

  /* Why us */
  .why-title { top: 2380px; font-size: 44px; }
  .benefit { top: 2455px; width: 300px; text-align: center; color: var(--ink); }
  .benefit svg { display: block; margin: 0 auto; }
  .benefit h3 { font-family: "Poppins", sans-serif; font-weight: 500; font-size: 19px; margin-top: 44px; }
  .benefit p { font-family: "Poppins", sans-serif; font-weight: 600; font-size: 13px; line-height: 17px; margin: 12px auto 0; width: 285px; text-transform: uppercase; }

  /* Footer */
  .site-footer { left: 0; top: 2876px; width: 1200px; height: 457px; background: var(--brand-red); }
  .site-footer .brand { left: 133px; top: 155px; }
  .site-footer .brand-name { font-size: 40px; }
  .site-footer .brand-dot { width: 36px; height: 36px; }
  .footer-email { left: 172px; top: 236px; font-weight: 700; font-size: 16px; color: var(--white); text-decoration: underline; }
  .social-dot { top: 280px; width: 41px; height: 41px; border-radius: 50%; background: var(--white); }
  .footer-links a { position: absolute; color: var(--white); text-decoration: none; font-size: 28px; font-weight: 700; }
  .copyright { left: 0; top: 375px; width: 1200px; text-align: center; font-family: "Poppins", sans-serif; font-weight: 600; font-size: 30px; color: var(--white); }
</style>
</head>
<body>

<header class="site-header abs">
  <div class="brand abs"><span class="brand-dot"></span><span class="brand-name">Brushvello Art</span></div>
  <nav class="main-nav abs">
    <a href="#">Home</a><a href="#">Shop</a><a href="#">Testomonials</a><a href="#">About Us</a><a href="#">FAQs</a><a href="#">My Orders</a><a href="#">Contact Us</a>
  </nav>
</header>

<h1 class="hero-title abs">Turn Your Digital Photos Into<br><span class="accent">One of a Kind</span> Wall Art</h1>

<div class="hero-collage abs" role="img" aria-label="Painted banner of a puppy, a child, a senior couple and a bride, with the original photos hanging beneath it"></div>

<h2 class="section-heading tagline abs">From Photo to Museum<br>Quality Canvas Art</h2>

<div class="feature-frame abs">
  <div class="feature-art abs" role="img" aria-label="Painted canvas of a shepherd dog resting with an orange cat, next to the original phone photo"></div>
  <a class="btn btn-start abs" href="#">Get Started</a>
</div>

<h2 class="section-heading categories-title abs">Categories</h2>
<div class="category-card cat-oil abs" role="img" aria-label="Oil painting style wedding couple"></div>
<div class="category-card cat-water abs" role="img" aria-label="Watercolor style mother and baby"></div>
<div class="category-card cat-digital abs" role="img" aria-label="Digital photo of a senior couple"></div>
<div class="category-card cat-impress abs" role="img" aria-label="Impressionist style bride with bouquet"></div>
<a class="btn category-btn abs" href="#" style="left:167px">Oil</a>
<a class="btn category-btn abs" href="#" style="left:403px">Water Color</a>
<a class="btn category-btn abs" href="#" style="left:642px">Digital Photo</a>
<a class="btn category-btn abs" href="#" style="left:879px;top:1866px">Impressionist</a>

<h2 class="section-heading about-title abs">About Us</h2>
<div class="about-copy abs">
  <p>At Brushvello Art, we take your digital photo and turn it into a one-of-a-kind piece of artwork!</p>
  <p>The process couldn’t be any easier. Simply upload your photo, choose your art style and size, and let our team of skilled digital artists do the rest. Do you want to put your digital photo on canvas without an art style? No problem! Just choose the “Digital Photo/Retouching” category and upload your photo. We can print your photo “as is” or do some minor retouching (e.g. remove objects, enhance colors, lighten photo, etc)</p>
  <p>You will receive a proof in your email to approve within 1-2 days. Once approved, your customized artwork will be transferred to canvas and shipped from our design studio in Florida.</p>
  <p>Brushvello Art makes a great gift for just about any special occasion. Know someone with an upcoming birthday, anniversary, housewarming party, wedding or other event? We’ve got you covered!</p>
  <p>Turn your cherished memories into a customized canvas masterpiece today!</p>
</div>

<h2 class="section-heading why-title abs">Why Us?</h2>

<div class="benefit abs" style="left:126px">
  <svg width="150" height="172" viewBox="0 0 150 172" fill="none" stroke="#1c1c28" stroke-width="5" stroke-linecap="round">
    <line x1="75" y1="4" x2="75" y2="24"/><line x1="30" y1="20" x2="42" y2="36"/><line x1="120" y1="20" x2="108" y2="36"/>
    <line x1="6" y1="50" x2="22" y2="58"/><line x1="144" y1="50" x2="128" y2="58"/>
    <path d="M52 126 C52 100 32 92 32 70 A43 43 0 0 1 118 70 C118 92 98 100 98 126 Z"/>
    <path d="M60 70 A18 18 0 0 1 90 60"/>
    <line x1="54" y1="138" x2="96" y2="138"/><line x1="56" y1="150" x2="94" y2="150"/><line x1="62" y1="162" x2="88" y2="162"/>
  </svg>
  <h3>YOUR IDEA YOUR DESIGN</h3>
  <p>Each art piece is customized for you! You choose your size, orientation and art style. Makes a perfect gift!!!</p>
</div>

<div class="benefit abs" style="left:449px">
  <svg width="160" height="172" viewBox="0 0 160 172" fill="none" stroke="#1c1c28" stroke-width="5" stroke-linecap="round" stroke-linejoin="round">
    <line x1="30" y1="10" x2="70" y2="10"/><line x1="20" y1="22" x2="60" y2="22"/><line x1="100" y1="10" x2="140" y2="10"/><path d="M140 10 a8 8 0 1 1 -8 8"/><line x1="110" y1="22" x2="130" y2="22"/>
    <rect x="8" y="40" width="98" height="96" rx="4"/>
    <path d="M42 40 v20 l12 -8 l12 8 v-20"/>
    <rect x="24" y="96" width="28" height="14" rx="2"/>
    <path d="M106 76 h28 l20 28 v32 h-48"/>
    <rect x="118" y="86" width="16" height="18"/>
    <circle cx="36" cy="146" r="12"/><circle cx="134" cy="146" r="12"/>
  </svg>
  <h3>FAST SHIPPING</h3>
  <p>Your artwork is printed and shipped in the USA! We offer fast turnaround with transit times typically 3-7 days.<br>Free tracking with each order!!</p>
</div>

<div class="benefit abs" style="left:760px">
  <svg width="130" height="172" viewBox="0 0 130 172" fill="none" stroke="#1c1c28" stroke-width="5" stroke-linejoin="round">
    <path d="M65 6 l12 8 14 -2 6 13 13 6 -2 14 8 12 -8 12 2 14 -13 6 -6 13 -14 -2 -12 8 -12 -8 -14 2 -6 -13 -13 -6 2 -14 -8 -12 8 -12 -2 -14 13 -6 6 -13 14 2 Z"/>
    <circle cx="65" cy="66" r="38"/>
    <path d="M65 46 l6 13 14 1 -11 9 4 14 -13 -8 -13 8 4 -14 -11 -9 14 -1 Z"/>
    <path d="M40 112 l-18 46 16 -4 10 14 18 -42"/><path d="M90 112 l18 46 -16 -4 -10 14 -18 -42"/>
  </svg>
  <h3>HIGH QUALITY</h3>
  <p>We’ve put a lot of effort ensuring your artwork is of the highest quality. Each piece is printed on the highest quality, gallery grade canvas.<br>It is ready to hang upon arrival.!</p>
</div>

<footer class="site-footer abs">
  <div class="brand abs"><span class="brand-dot"></span><span class="brand-name">Brushvello Art</span></div>
  <a class="footer-email abs" href="#">info@brushvellomart.com</a>
  <span class="social-dot abs" style="left:212px" aria-label="Social profile"></span>
  <span class="social-dot abs" style="left:286px" aria-label="Social profile"></span>
  <nav class="footer-links">
    <a href="#" style="left:520px;top:115px">Get Started</a>
    <a href="#" style="left:524px;top:172px">My Orders</a>
    <a href="#" style="left:523px;top:229px">About Us</a>
    <a href="#" style="left:523px;top:288px">Testomonials</a>
    <a href="#" style="left:804px;top:115px">FAQs</a>
    <a href="#" style="left:804px;top:172px">Contact Us</a>
    <a href="#" style="left:804px;top:224px">Privacy Policy</a>
    <a href="#" style="left:804px;top:286px">Terms and Conditions</a>
  </nav>
  <p class="copyright abs">© Brushvello Art 2023. All rights reserved.</p>
</footer>

</body>
</html>
```